Dental Office Business Card

We need a business card for our pediatric dentistry office.
On one side the design needs to contain the following:
our logo (attached)
Vento Pediatric Grins
Soraya Kadbelani, DDS
Board Certified Pediatric Dentist
Tel: (555) 318-2747)
Fax: (555) 264-8031
Email: info@ventopediatricgrins.example
Web: www.ventopediatricgrins.example
Address: 41 Brindle Ave, Suite 208, Larkridge, QX 02099

On the other side of the card, the design needs to have an appointment reminder (date and time as well as day of the week) similar to the design attached (no need for appointment reason “For”)

```html
<!DOCTYPE html>
<html lang="en">
<head>
<meta charset="utf-8">
<title>Vento Pediatric Grins – Business Card</title>
<link rel="stylesheet" href="https://fonts.googleapis.com/css2?family=Montserrat:wght@400;500;600;700&display=swap">
<style>
  :root {
    --mint: #a3dbb0;
    --mint-text: #8fd3a0;
    --ink: #1b1b1b;
    --paper: #ffffff;
    --backdrop: #e9ebea;
  }
  * { box-sizing: border-box; margin: 0; padding: 0; }
  html, body { width: 1200px; height: 1200px; overflow: hidden; }
  body {
    background: var(--backdrop);
    font-family: "Montserrat", sans-serif;
    color: var(--ink);
    display: flex;
    flex-direction: column;
    align-items: center;
    justify-content: center;
    gap: 60px;
  }
  .card {
    position: relative;
    width: 860px;
    height: 491px;
    background: var(--paper);
    border-radius: 34px;
    overflow: hidden;
    box-shadow: 0 10px 28px rgba(0,0,0,0.14);
  }

  /* Front: contact + appointment */
  .contact { position: absolute; left: 56px; top: 56px; }
  .contact__name {
    font-size: 25px; font-weight: 600; color: var(--mint-text);
    text-transform: uppercase; letter-spacing: 0.5px; white-space: nowrap;
  }
  .contact__title {
    font-size: 14px; font-weight: 500; text-transform: uppercase;
    letter-spacing: 0.4px; margin-top: 2px; white-space: nowrap;
  }
  .contact__list { list-style: none; margin-top: 16px; font-size: 15px; line-height: 24px; }
  .contact__list li { display: flex; align-items: center; gap: 10px; white-space: nowrap; }
  .contact__icon { width: 16px; height: 16px; flex: none; fill: var(--mint-text); }
  .contact__address { margin-top: 14px; margin-left: 26px; font-size: 15px; line-height: 20px; }

  .brand { position: absolute; display: flex; align-items: center; gap: 16px; }
  .brand__dot { border-radius: 50%; background: var(--mint); flex: none; }
  .brand__name { font-weight: 700; color: var(--ink); line-height: 1.05; white-space: nowrap; }
  .brand--front { right: 56px; top: 70px; }
  .brand--front .brand__dot { width: 54px; height: 54px; }
  .brand--front .brand__name { font-size: 34px; }

  .appointment { position: absolute; left: 56px; right: 56px; top: 318px; font-size: 18px; }
  .appointment__row { display: flex; align-items: flex-end; gap: 10px; }
  .appointment__line { flex: 1; border-bottom: 1.5px solid var(--ink); height: 20px; }
  .appointment__ampm { font-size: 15px; }
  .days { display: flex; justify-content: space-between; margin-top: 32px; }
  .day { display: flex; align-items: center; gap: 10px; }
  .day__box { width: 30px; height: 30px; border: 1.5px solid var(--ink); }

  .card__band { position: absolute; left: 0; bottom: 0; width: 860px; height: 30px; }

  /* Back: brand */
  .brand--back { left: 50%; top: 50%; transform: translate(-50%, -50%); gap: 26px; }
  .brand--back .brand__dot { width: 96px; height: 96px; }
  .brand--back .brand__name { font-size: 58px; }
</style>
</head>
<body>

<section class="card card--front" aria-label="Card front with contact details and appointment reminder">
  <div class="contact">
    <p class="contact__name">Soraya Kadbelani, DDS</p>
    <p class="contact__title">Board Certified Pediatric Dentist</p>
    <ul class="contact__list">
      <li><svg class="contact__icon" viewBox="0 0 16 16" aria-hidden="true"><path d="M3 1l3 3-1.5 2a9 9 0 0 0 5.5 5.5L12 10l3 3-2 2C7 15 1 9 1 3z"/></svg>(555) 318-2747)</li>
      <li><svg class="contact__icon" viewBox="0 0 16 16" aria-hidden="true"><path d="M4 1h7v4H4zM1 6h14v9H1zm3 3h2v2H4zm4 0h2v2H8zm4 0h1v5h-1z"/></svg>(555) 264-8031</li>
      <li><svg class="contact__icon" viewBox="0 0 16 16" aria-hidden="true"><path d="M1 3h14v10H1zm1 1l6 5 6-5v1l-6 5-6-5z"/></svg>info@ventopediatricgrins.example</li>
      <li><svg class="contact__icon" viewBox="0 0 16 16" aria-hidden="true"><path d="M8 1a7 7 0 1 0 0 14A7 7 0 0 0 8 1zm0 1.5c1 1 1.7 2.6 1.9 4.5H6.1C6.3 5.1 7 3.5 8 2.5zM2.6 7h2.3c.1 1.6.5 3.1 1.2 4.2A5.6 5.6 0 0 1 2.6 7zm0 2h2.3M7 9h2c-.2 1.6-.6 3-1 4-.4-1-.8-2.4-1-4zm4.1-2h2.3a5.6 5.6 0 0 1-3.5 4.2c.7-1.1 1.1-2.6 1.2-4.2z"/></svg>www.ventopediatricgrins.example</li>
    </ul>
    <p class="contact__address">41 Brindle Ave, Suite 208,<br>Larkridge, QX 02099</p>
  </div>

  <div class="brand brand--front">
    <span class="brand__dot"></span>
    <span class="brand__name">Vento<br>Pediatric Grins</span>
  </div>

  <div class="appointment">
    <div class="appointment__row">
      <span>Date:</span><span class="appointment__line"></span>
      <span>Time:</span><span class="appointment__line"></span>
      <span class="appointment__ampm">a.m&nbsp;&nbsp;p.m</span>
    </div>
    <div class="days">
      <span class="day"><span class="day__box"></span>Mon</span>
      <span class="day"><span class="day__box"></span>Tue</span>
      <span class="day"><span class="day__box"></span>Wed</span>
      <span class="day"><span class="day__box"></span>Thu</span>
      <span class="day"><span class="day__box"></span>Fri</span>
      <span class="day"><span class="day__box"></span>Sat</span>
      <span class="day"><span class="day__box"></span>Sun</span>
    </div>
  </div>

  <svg class="card__band" viewBox="0 0 860 30" preserveAspectRatio="none" aria-hidden="true">
    <polygon points="0,18 560,0 552,30 0,30" fill="var(--mint)"/>
    <polygon points="572,0 860,0 860,30 564,30" fill="var(--ink)"/>
  </svg>
</section>

<section class="card card--back" aria-label="Card back with practice name">
  <div class="brand brand--back">
    <span class="brand__dot"></span>
    <span class="brand__name">Vento<br>Pediatric Grins</span>
  </div>
</section>

</body>
</html>
```